Inner pages for KRB Accelerate

***PLEASE NOTE***
Please do not vie for this project if you were not invited. This project was meant for a particular designer but was erroneously created as a contest. Thank you.
**********

I need HTML/CSS files for the design that was done for the front page attached.
I also need designs and HTML for these inner pages to match the template:
http://www.krb-accelerate.example/documentation/how-the-plugin-works.html
http://www.krb-accelerate.example/support/knowlegebase.html
http://www.krb-accelerate.example/support/knowlegebase.html?View=entry&EntryID=9
http://www.krb-accelerate.example/subscribe/new.html
http://www.krb-accelerate.example/downloads.html

For the downloads page (http://www.krb-accelerate.example/downloads.html), I'm going to be providing download links to files for four different platforms. (That's the plan anyway) So that row that has the Download/Subscribe buttons would be repeated 4 times, one for each platform (That's shown on the front page)

```html
<!DOCTYPE html>
<html lang="en">
<head>
<meta charset="utf-8">
<title>Knowledgebase – KRB Accelerate</title>
<link href="https://fonts.googleapis.com/css2?family=Lato:wght@300;400;700;900&display=swap" rel="stylesheet">
<style>
:root{
  --green:#6aad37;
  --green-light:#8cc462;
  --green-text:#7cb342;
  --ink:#111;
  --text:#555;
  --muted:#777;
  --page:#f7f7f7;
  --line:#e2e2e2;
  --dark:#5e5e5e;
  --dark-btn:#5a5a5a;
  --footer-text:#c9c9c9;
}
*{box-sizing:border-box;margin:0;padding:0}
html,body{width:1018px;height:1200px;overflow:hidden}
body{background:var(--page);font-family:'Lato',sans-serif;color:var(--text);position:relative}
.wrap{position:absolute;left:116px;width:784px}

/* header */
.site-header{position:absolute;top:0;left:0;width:1018px;height:90px;background:var(--page)}
.brand{position:absolute;left:116px;top:42px;display:flex;align-items:center;gap:8px;font-size:26px;font-weight:900;color:var(--dark-btn);letter-spacing:-.3px}
.brand-mark{width:18px;height:18px;background:var(--green)}
.main-nav{position:absolute;top:8px;left:463px;display:flex;gap:20px;font-size:12px;color:#666}
.main-nav .active{color:var(--green);margin-right:12px}
.login{position:absolute;left:837px;top:1px;width:63px;height:26px;background:var(--dark-btn);color:#fff;font-size:11px;display:flex;align-items:center;justify-content:center;gap:5px}
.site-search{position:absolute;left:675px;top:45px;display:flex}
.site-search .field{width:150px;height:26px;border:1px solid #555;background:#fff;font-size:10px;color:#777;padding:7px 7px}
.site-search .btn{width:75px;height:26px;background:var(--dark-btn);color:#fff;font-size:12px;font-weight:700;display:flex;align-items:center;justify-content:center}

/* banner */
.banner{position:absolute;top:90px;left:0;width:1018px;height:188px;background:radial-gradient(ellipse 260px 120px at 509px 95px,var(--green-light),var(--green))}
.banner .crumbs{position:absolute;left:119px;top:18px;font-size:11px;font-weight:700;color:#fff}
.banner h2{position:absolute;left:355px;width:335px;top:64px;height:61px;border-top:1px solid rgba(255,255,255,.25);border-bottom:1px solid rgba(255,255,255,.25);text-align:center;color:#fff;font-size:37px;font-weight:900;line-height:59px}

/* content */
.page-title{top:292px;font-size:33px;font-weight:900;color:var(--ink)}
.page-crumbs{top:342px;font-size:10px;color:var(--muted);word-spacing:2px}
.kb-panel{top:377px;height:108px;background:#fff;border:1px solid #e6e6e6}
.kb-panel .label{position:absolute;font-size:15px;font-weight:700;color:#666}
.kb-panel .label small{font-weight:300;font-size:12px;color:#777;margin-left:12px}
.kb-panel .input{position:absolute;top:53px;height:28px;background:#f3f3f3;border:1px solid #d6d6d6}
.kb-panel .go{position:absolute;top:53px;height:28px;background:var(--green);color:#fff;font-size:13px;font-weight:700;display:flex;align-items:center;justify-content:center;gap:6px}
.kb-label{top:502px;font-size:11px;color:#666}
.section-bar{top:533px;height:25px;background:var(--green);color:#fff;font-size:12px;font-weight:700;padding:6px 9px}
.entries{top:570px;list-style:none}
.entry{border-bottom:1px solid var(--line);padding:10px 0 10px;height:80px}
.entry h3{font-size:12px;font-weight:700;color:var(--ink)}
.entry p{font-size:9.5px;color:#777;margin-top:7px}
.entry .meta{margin-top:6px;font-size:9.5px;font-weight:700;color:var(--green-text);display:flex;gap:12px}
.entry .meta span:last-child{margin-left:10px}
.powered{top:900px;font-size:9px;color:#666;padding-left:2px}

/* footer */
.site-footer{position:absolute;top:958px;left:0;width:1018px;height:242px;background:linear-gradient(180deg,#5c5c5c,#606060 60%,#585858)}
.footer-links{position:absolute;left:132px;top:29px;display:flex;gap:14px;font-size:11px;color:var(--footer-text)}
.footer-links .sep{color:#aaa}
.footer-rule{position:absolute;left:116px;width:784px;height:1px;background:rgba(255,255,255,.12)}
.copyright{position:absolute;left:116px;top:108px;font-size:11px;color:var(--footer-text)}
.footer-brand{position:absolute;left:0;width:1018px;top:90px;text-align:center;font-size:24px;font-weight:900;color:#cfcfcf}
.legal{position:absolute;right:118px;top:108px;display:flex;gap:13px;font-size:11px;color:var(--footer-text)}
.license{position:absolute;left:116px;top:194px;font-size:11px;color:var(--green)}
.social{position:absolute;left:816px;top:196px;display:flex;gap:8px}
.social span{width:22px;height:22px;border-radius:3px}
.social .s1{background:#2aa9e0}.social .s2{background:#3b5b9a}.social .s3{background:#d9433a}
</style>
</head>
<body>

<header class="site-header">
  <div class="brand"><span class="brand-mark"></span>KRB Accelerate</div>
  <nav class="main-nav">
    <span class="active">Home</span><span>Documentation</span><span>Support</span><span>Downloads</span><span>Subscribe</span>
  </nav>
  <div class="login">
    <svg width="12" height="12" viewBox="0 0 12 12" fill="none" stroke="#fff" stroke-width="1.2"><circle cx="6" cy="4" r="2.6"/><path d="M1.5 11.3c.4-2.6 2.2-3.8 4.5-3.8s4.1 1.2 4.5 3.8z"/></svg>
    Login
  </div>
  <div class="site-search"><div class="field">Enter Your Keyword</div><div class="btn">Search</div></div>
</header>

<section class="banner" role="img" aria-label="Green banner with faint speech bubble pattern">
  <div class="crumbs">You are here:Home&nbsp; / &nbsp;Documentation&nbsp; / &nbsp;How the plugin works</div>
  <h2>FAQs</h2>
</section>

<main>
  <h1 class="wrap page-title">Knowledgebase</h1>
  <div class="wrap page-crumbs">You are here:Home &nbsp; / &nbsp; Support &nbsp; / &nbsp; FAQ Knowlegebase</div>

  <div class="wrap kb-panel">
    <div class="label" style="left:17px;top:22px">Search:<small>Advanced Search</small></div>
    <div class="input" style="left:16px;width:288px"></div>
    <div class="go" style="left:307px;width:61px">
      <svg width="15" height="15" viewBox="0 0 15 15" fill="none" stroke="#fff" stroke-width="1.6"><circle cx="6" cy="6" r="4.5"/><path d="M9.5 9.5l4.5 4.5"/></svg>GO
    </div>
    <div class="label" style="left:420px;top:25px">Browse by Category:</div>
    <div class="input" style="left:419px;width:287px"></div>
    <div class="go" style="left:711px;width:61px">
      <svg width="16" height="15" viewBox="0 0 16 15" fill="none" stroke="#fff" stroke-width="1.2"><path d="M8 1l7 3-7 3-7-3z"/><path d="M1 7.5l7 3 7-3"/><path d="M1 11l7 3 7-3"/></svg>GO
    </div>
  </div>

  <div class="wrap kb-label">Knowledgebase</div>
  <div class="wrap section-bar">Most viewed</div>

  <ul class="wrap entries">
    <li class="entry"><h3>Failed fetching links... error in backend.</h3><p>The plugin is trying to make a cURL call to your home page so it can parse the contents for the CSS/Js links the plugin will find to combine. It uses...</p><div class="meta"><span>Not rated</span><span>28 Mar, 2014</span><span>Views: 4188</span></div></li>
    <li class="entry"><h3>Failed fetching links... error in backend.</h3><p>The plugin is trying to make a cURL call to your home page so it can parse the contents for the CSS/Js links the plugin will find to combine. It uses...</p><div class="meta"><span>Not rated</span><span>28 Mar, 2014</span><span>Views: 4188</span></div></li>
    <li class="entry"><h3>Failed fetching links... error in backend.</h3><p>The plugin is trying to make a cURL call to your home page so it can parse the contents for the CSS/Js links the plugin will find to combine. It uses...</p><div class="meta"><span>Not rated</span><span>28 Mar, 2014</span><span>Views: 4188</span></div></li>
    <li class="entry"><h3>Failed fetching links... error in backend.</h3><p>The plugin is trying to make a cURL call to your home page so it can parse the contents for the CSS/Js links the plugin will find to combine. It uses...</p><div class="meta"><span>Not rated</span><span>28 Mar, 2014</span><span>Views: 4188</span></div></li>
  </ul>

  <div class="wrap powered">Powered by DocuBase (Knowledge base software)</div>
</main>

<footer class="site-footer">
  <nav class="footer-links">
    <span>Portalis</span><span class="sep">|</span><span>Gridwork Kit</span><span class="sep">|</span><span>Stylo Website</span><span class="sep">|</span><span>HTML5</span><span class="sep">|</span><span>Framewise Website</span><span class="sep">|</span><span>Glyph Set</span><span class="sep">|</span><span>Downloads</span>
  </nav>
  <div class="footer-rule" style="top:63px"></div>
  <div class="copyright">Copyright © 2013 KRB Accelerate, All rights reserved.</div>
  <div class="footer-brand">KRB Accelerate</div>
  <nav class="legal"><span>Terms of Use</span><span>Privacy Policy</span><span>Refund Policy</span><span>Contact Us</span></nav>
  <div class="footer-rule" style="top:172px"></div>
  <div class="license">KRB Accelerate is released under the GNU General Public License.</div>
  <div class="social"><span class="s1"></span><span class="s2"></span><span class="s3"></span></div>
</footer>

</body>
</html>
```